Specialized Personal Trainer Needs a Business Card Design

I need a business card design for my personal training business called Tall Oak Fitness. I have my Human Kinetics degree in Exercise Science from the Halvern Ridge University as well as an extra certification from NBEP (National Board of Exercise Practice). I work as a Cardiac Rehab Exercise Specialist and personal trainer giving specialized exercise prescriptions to those that have different heart conditions as well as work with the general population in weight loss, strength and conditioning, getting/staying fit.
Updates

I decided that I wanted a logo (as I did not have one before I submitted my project for a business card) so I am submitting a project to get a logo done and then I will decide on a business card, hopefully being able to use one of the designs already submitted.  My apologies for doing this backwards.  I am new to this so I appreciate your patience.

Thank you.

Hi, I have just created a project for a logo design (I realized I needed a logo and I should've done that first..oops!), please feel free to participate.  Once I receive a logo I like I will finalize my business card project and hopefully incorporate it into one of your business card designs. 

Thank you!

Target Market(s)

Business professionals

Industry/Entity Type

Personal Trainer

Requirements
Must have
• My name with my info:
Celia R. Dunhill (BHK)
NBEP Certified Clinical Exercise Specialist & Personal Trainer
celia.dunhill@talloakfitness.example
Cell: 604-358-4170

Please make it double sided.
Nice to have
• An image that represents cardiac and general fitness training.

```html
<!DOCTYPE html>
<html lang="en">
<head>
<meta charset="utf-8">
<title>Celia R. Dunhill — Business Card</title>
<link rel="stylesheet" href="https://fonts.googleapis.com/css2?family=Courier+Prime:wght@400&display=swap">
<style>
  :root {
    --backdrop: #86a079;
    --card: #e7e7e9;
    --ink: #34414c;
    --heart: #58261c;
  }
  html, body {
    margin: 0;
    padding: 0;
    width: 1200px;
    height: 1200px;
    overflow: hidden;
    background: var(--backdrop);
  }
  .canvas {
    position: relative;
    width: 1200px;
    height: 1200px;
    font-family: "Courier Prime", "Courier New", monospace;
    color: var(--ink);
  }
  .card {
    position: absolute;
    left: 276px;
    width: 650px;
    height: 377px;
    background: var(--card);
  }
  .card-front { top: 211px; }
  .card-back  { top: 610px; }

  .name {
    position: absolute;
    left: 49px;
    top: 62px;
    margin: 0;
    font-size: 27px;
    line-height: 32px;
    font-weight: 400;
    letter-spacing: 1px;
    white-space: nowrap;
  }
  .name-rule {
    position: absolute;
    left: 0;
    top: 101px;
    width: 576px;
    height: 3px;
    background: var(--ink);
  }
  .credentials {
    position: absolute;
    left: 49px;
    top: 118px;
    margin: 0;
    font-size: 18px;
    line-height: 24px;
    letter-spacing: 0.6px;
    white-space: nowrap;
  }
  .contact {
    position: absolute;
    left: 49px;
    top: 270px;
    font-size: 18px;
    line-height: 23px;
    letter-spacing: 0.6px;
    white-space: nowrap;
  }
  .contact-label {
    display: block;
    font-size: 13px;
    line-height: 18px;
    margin-bottom: 4px;
  }
  .emblem-area {
    position: absolute;
    left: 179px;
    top: 77px;
    width: 292px;
    height: 240px;
    background: linear-gradient(180deg, var(--heart) 0%, var(--ink) 100%);
    opacity: 0.85;
  }
</style>
</head>
<body>
<main class="canvas">
  <section class="card card-front">
    <h1 class="name">Celia R. Dunhill (BHK)</h1>
    <div class="name-rule"></div>
    <p class="credentials">NBEP Certified Clinical Exercise Specialist<br>&amp; Personal Trainer</p>
    <div class="contact">
      <span class="contact-label">contact:</span>
      celia.dunhill@talloakfitness.example<br>
      604-358-4170
    </div>
  </section>

  <section class="card card-back">
    <div class="emblem-area" role="img" aria-label="Emblem of a heart above a barbell, representing cardiac and fitness training"></div>
  </section>
</main>
</body>
</html>
```